Orvex Panel Flyer

I need a flyer designed for our Orvex Panel software service. Basically most of the content that is on the website (orvexpanel.com.au) but I have uploaded a couple of source files as well. Please continue with this blue colour scheme

Target Market(s)

Business owners

Industry/Entity Type

Software

Font styles to use
Sans Serif

Colors
0456a4

Requirements
Must have
• Content from orvexpanel.com.au and similar theme

```html
<!DOCTYPE html>
<html lang="en">
<head>
<meta charset="utf-8">
<title>Orvex Panel Flyer</title>
<link rel="stylesheet" href="https://fonts.googleapis.com/css2?family=Montserrat:wght@500;800&display=swap">
<style>
  :root {
    --blue-base: #1566b6;
    --blue-deep: #0b57a4;
    --blue-mid: #1f7fcc;
    --blue-sky: #1cb2ea;
    --blue-light: #35b9ee;
    --blue-band: #3f78b8;
    --blue-pale: #6aa9d9;
    --lime: #d5e02b;
    --white: #f4f4f4;
  }
  html, body {
    margin: 0;
    padding: 0;
    overflow: hidden;
    background: var(--blue-base);
  }
  .flyer {
    position: relative;
    width: 848px;
    height: 1200px;
    overflow: hidden;
    font-family: "Montserrat", Arial, sans-serif;
    background: var(--blue-base);
  }
  .backdrop {
    position: absolute;
    inset: 0;
  }
  .brand-name {
    position: absolute;
    left: 200px;
    top: 188px;
    width: 480px;
    margin: 0;
    text-align: center;
    color: var(--white);
    font-weight: 800;
    font-size: 86px;
    line-height: 96px;
    letter-spacing: 1px;
    text-transform: uppercase;
  }
  .headline {
    position: absolute;
    right: 40px;
    top: 446px;
    margin: 0;
    text-align: right;
    color: var(--white);
    font-weight: 800;
    font-size: 75px;
    line-height: 72px;
    letter-spacing: 1px;
    text-transform: uppercase;
  }
  .web-address {
    position: absolute;
    left: 0;
    right: 0;
    top: 1146px;
    margin: 0;
    text-align: center;
    color: var(--lime);
    font-weight: 500;
    font-size: 15px;
    letter-spacing: 0.3px;
    text-transform: uppercase;
  }
  .hatch-band {
    position: absolute;
    left: 0;
    top: 477px;
    width: 229px;
    height: 50px;
    background: repeating-linear-gradient(-45deg, var(--lime) 0 11px, transparent 11px 22px);
  }
  .white-bar {
    position: absolute;
    height: 22px;
    background: var(--white);
  }
  .white-bar--upper { left: 94px; top: 435px; width: 152px; }
  .white-bar--lower { left: 662px; top: 1033px; width: 152px; }
</style>
</head>
<body>
<div class="flyer">
  <svg class="backdrop" width="848" height="1200" viewBox="0 0 848 1200" aria-hidden="true">
    <!-- geometric panels -->
    <rect width="848" height="1200" fill="var(--blue-base)"/>
    <polygon points="0,0 480,0 150,60 0,110" fill="var(--blue-deep)"/>
    <polygon points="0,110 150,60 420,360 0,330" fill="var(--blue-mid)" opacity="0.55"/>
    <polygon points="440,0 848,0 848,330 700,260" fill="var(--blue-sky)"/>
    <polygon points="480,0 700,260 560,520 300,260" fill="var(--blue-mid)" opacity="0.8"/>
    <polygon points="700,260 848,330 848,720 640,560" fill="var(--blue-light)" opacity="0.9"/>
    <polygon points="560,520 700,260 640,560" fill="var(--blue-sky)" opacity="0.6"/>
    <polygon points="0,330 420,360 300,700 0,640" fill="var(--blue-deep)" opacity="0.35"/>
    <polygon points="420,360 640,560 520,803 300,700" fill="var(--blue-mid)" opacity="0.45"/>
    <polygon points="640,560 848,720 848,803 520,803" fill="var(--blue-mid)" opacity="0.7"/>
    <!-- lower band -->
    <rect x="0" y="803" width="848" height="397" fill="var(--blue-band)"/>
    <polygon points="85,803 330,803 230,1010 0,1080 0,940" fill="var(--blue-pale)"/>
    <polygon points="330,803 560,803 410,1200 150,1200 230,1010" fill="var(--blue-pale)" opacity="0.45"/>
    <polygon points="0,1080 230,1010 150,1200 0,1200" fill="var(--blue-base)" opacity="0.55"/>
    <polygon points="560,803 848,803 848,1200 700,1200" fill="var(--blue-band)" opacity="0.6"/>

    <!-- top stripe row -->
    <g fill="var(--lime)">
      <rect x="545" y="94" width="9" height="48"/>
      <rect x="571" y="94" width="9" height="48"/>
      <rect x="597" y="94" width="9" height="48"/>
      <rect x="623" y="94" width="9" height="48"/>
      <rect x="649" y="94" width="9" height="48"/>
      <rect x="675" y="94" width="9" height="48"/>
      <rect x="701" y="94" width="9" height="48"/>
      <rect x="727" y="94" width="9" height="48"/>
      <rect x="753" y="94" width="9" height="48"/>
      <rect x="779" y="94" width="9" height="48"/>
      <rect x="805" y="94" width="9" height="48"/>
      <rect x="831" y="94" width="9" height="48"/>
    </g>

    <!-- bottom-left stripe row -->
    <g fill="var(--lime)">
      <rect x="6" y="943" width="9" height="50"/>
      <rect x="28" y="943" width="9" height="50"/>
      <rect x="50" y="943" width="9" height="50"/>
      <rect x="72" y="943" width="9" height="50"/>
      <rect x="94" y="943" width="9" height="50"/>
      <rect x="116" y="943" width="9" height="50"/>
      <rect x="138" y="943" width="9" height="50"/>
    </g>

    <!-- triangles -->
    <polygon points="75,226 107,226 91,254" fill="var(--lime)"/>
    <polygon points="40,713 86,713 63,754" fill="var(--lime)"/>
    <polygon points="419,1057 454,1116 384,1116" fill="var(--lime)"/>

    <!-- wave -->
    <path d="M622,998 q14,-16 29,0 t29,0 t29,0 t29,0 t29,0 t29,0 t29,0 t29,0"
          fill="none" stroke="var(--lime)" stroke-width="8" stroke-linecap="round"/>
  </svg>

  <div class="hatch-band" aria-hidden="true"></div>
  <div class="white-bar white-bar--upper" aria-hidden="true"></div>
  <div class="white-bar white-bar--lower" aria-hidden="true"></div>

  <h1 class="brand-name">Orvex<br>Panel</h1>

  <p class="headline">Keep<br>your<br>finger<br>on the<br>pulse of<br>your<br>business.</p>

  <p class="web-address">http://orvexpanel.com.au/</p>
</div>
</body>
</html>
```